Postcard Design

I need a postcard to use as a mailer and handout piece to get a new vacation rental management company off the ground. This will be sent to rental property owners in Merindel on 30a in Florida.

A google image search of "Merindel 30A" will provide plenty of images for look and feel of the project. A quick google of "coastal modern design" will provide some feel for interiors and a color palette using the beachy but subtle colors typical to that decor.

Merindel is a 130 unit condominium complex in a very active beach rental market. The tone of the community is upscale family vacations...it is NOT a party destination. Beach and family time are what most people are here for.

Logo file uploaded here.

If good design comes in quickly I may zero in on one quickly to tweak it and get things moving.

Target audience is property owners who we hope to bring in as rental owners. The audience is not rental guests. Try to sell to property owners who you want to trust us with their investments.

We offer a full lineup of services including top-notch housekeeping, maintenance, marketing, and guest services.

We want to build relationships with our property owners.

We are a small team focused on only Merindel properties.

Designers...please feel free to suggest any wording or tag lines that you think sell this idea. Your creativity with the copy is as valuable as your visual creativity.

Some copy scraps & messaging to play with:

Tailored exclusively to Merindel and its owners

Boutique Rental Management

Full service maintenance and housekeeping

Merindel's reputation is our reputation

Thank you all.

I just updated he brief to provide some added guidance. Thanks!

Boutique

```html
<!DOCTYPE html>
<html lang="en">
<head>
<meta charset="utf-8">
<title>Merindel Boutique Rental Management – Postcard</title>
<link rel="stylesheet" href="https://fonts.googleapis.com/css2?family=Roboto+Condensed:wght@400&family=Roboto:wght@400&display=swap">
<style>
  :root {
    --page-bg: #ffffff;
    --accent-orange: #d9744a;
    --band-sea: #8bbcaa;
    --band-sand: #ddcfa9;
    --ink: #3b2a22;
    --back-mist: #e4ede8;
    --stamp-sea: #b0cdc4;
    --rule: #5a4a42;
    --white: #ffffff;
  }
  * { box-sizing: border-box; margin: 0; padding: 0; }
  html, body {
    width: 1200px;
    height: 1000px;
    overflow: hidden;
    background: var(--page-bg);
  }
  .canvas {
    position: relative;
    width: 1200px;
    height: 1000px;
  }
  .postcard {
    position: absolute;
    top: 304px;
    width: 507px;
    height: 391px;
    overflow: hidden;
  }
  .postcard--front { left: 69px; background: var(--white); }
  .postcard--back  { left: 624px; background: var(--back-mist); }

  /* Front: photo collage */
  .photo { position: absolute; }
  .photo--resort {
    left: 0; top: 0; width: 251px; height: 176px;
    background: linear-gradient(180deg, #b9d3ea 0%, #d8c79a 45%, #8fa86a 70%, #5fb1c9 100%);
  }
  .photo--beach {
    left: 256px; top: 43px; width: 120px; height: 133px;
    background: linear-gradient(180deg, #9fd0c8 0%, #cfe6df 40%, #f2efe8 75%, #e9e4da 100%);
  }
  .photo--boardwalk {
    left: 381px; top: 0; width: 126px; height: 96px;
    background: linear-gradient(180deg, #7fb7e6 0%, #bfd9ea 35%, #9a8a72 65%, #6e6253 100%);
  }
  .photo--pool {
    left: 381px; top: 101px; width: 126px; height: 75px;
    background: linear-gradient(180deg, #bcd6ea 0%, #78b7c7 35%, #8ecfd8 65%, #c7b79a 100%);
  }

  .headline-banner {
    position: absolute;
    left: 0; top: 0;
    width: 390px; height: 43px;
    background: var(--accent-orange);
    color: var(--white);
    font-family: "Roboto Condensed", "Arial Narrow", sans-serif;
    font-size: 22px;
    line-height: 43px;
    padding-left: 16px;
    white-space: nowrap;
  }

  .pitch-band {
    position: absolute;
    left: 0; top: 181px;
    width: 507px; height: 130px;
    background: var(--band-sea);
    padding: 15px 26px 0 26px;
    font-family: "Roboto Condensed", "Arial Narrow", sans-serif;
    font-size: 11.3px;
    line-height: 14.5px;
    color: var(--ink);
  }
  .pitch-band p { margin-bottom: 10px; }

  .contact-band {
    position: absolute;
    left: 0; top: 316px;
    width: 507px; height: 75px;
    background: var(--band-sand);
  }
  .contact-details {
    position: absolute;
    left: 26px; top: 31px;
    font-family: "Roboto", Arial, sans-serif;
    font-size: 9.6px;
    line-height: 13px;
    color: var(--ink);
  }
  .contact-details .company { color: #2e221c; }

  .wordmark {
    position: absolute;
    font-family: "Roboto Condensed", "Arial Narrow", sans-serif;
    font-weight: 400;
    color: var(--ink);
    white-space: nowrap;
  }
  .contact-band .wordmark {
    right: 30px; top: 18px;
    font-size: 34px;
    line-height: 40px;
  }

  /* Back */
  .address-divider {
    position: absolute;
    left: 244px; top: 25px;
    width: 1px; height: 296px;
    background: var(--rule);
  }
  .stamp-box {
    position: absolute;
    left: 394px; top: 25px;
  }
  .postcard--back .wordmark {
    left: 26px; top: 172px;
    font-size: 40px;
    line-height: 46px;
  }
  .address-lines {
    position: absolute;
    left: 288px; top: 180px;
    width: 190px;
    list-style: none;
  }
  .address-lines li {
    height: 1px;
    background: var(--rule);
    margin-bottom: 35px;
  }
</style>
</head>
<body>
<main class="canvas">

  <!-- Front of postcard -->
  <section class="postcard postcard--front" aria-label="Postcard front">
    <div class="photo photo--resort" role="img" aria-label="Photo of the condominium resort with a pool and fountain"></div>
    <div class="photo photo--beach" role="img" aria-label="Photo of white sand beach with beach chairs"></div>
    <div class="photo photo--boardwalk" role="img" aria-label="Photo of a wooden boardwalk leading to the sea"></div>
    <div class="photo photo--pool" role="img" aria-label="Photo of a pool overlooking the beach"></div>

    <h1 class="headline-banner">We know how to improve your incomes</h1>

    <div class="pitch-band">
      <p>We are a small team of Merindel's Condo experts.</p>
      <p>Find your investment opportunity here at the beautiful Merindel by Harborline.</p>
      <p>Let our real estate professionals&nbsp; personally assist you.</p>
      <p>We offer state of the art marketing, complete guest services, top notch housekeeping and all year round maintenance.</p>
    </div>

    <div class="contact-band">
      <div class="contact-details">
        <div class="company">Merindel's Boutique Rental Management</div>
        <div class="phone">Contact us at: Toll Free: (866) 555-0148</div>
      </div>
      <div class="wordmark">Merindel</div>
    </div>
  </section>

  <!-- Back of postcard -->
  <section class="postcard postcard--back" aria-label="Postcard back">
    <div class="wordmark">Merindel</div>
    <div class="address-divider"></div>
    <svg class="stamp-box" width="84" height="93" viewBox="0 0 84 93" aria-hidden="true">
      <rect x="2" y="2" width="80" height="89" fill="var(--stamp-sea)"/>
    </svg>
    <ul class="address-lines" aria-label="Address lines">
      <li></li><li></li><li></li><li></li><li></li>
    </ul>
  </section>

</main>
</body>
</html>
```